harborKettrix.com Blog/website

This is new site, we do not have any current content
Would like a website for harbor kettrix. The site will cover what to expect getting started, what to wear. How to pick out a kettrix Gym (called a box).
We will be posting articles on exercises and how to properly perform and occasional product review.
We would like a section on recipes and what to eat and not to eat
We are attempting to remove the barrier of entry to get new people transform their lives/body and try kettrix.
Will also like to post daily Work outs which are called WODs (workout of the day) and exercises.
The sections of the site I envision are
• the front landing page
• Contact Page
• Blog Page
• About Page
• Recipe Page
• Exercise Page
• FAQ and frequently used Terms

Target Market(s)

Fitness market, people interested or just starting kettrix

Industry/Entity Type

Fitness

Logo Text

harbor Kettrix - your kettrix start page - or something like that

Coding

Coded - Design and coding required

Number of Pages Required

5+ page

Font styles to use
Sans Serif

Requirements
Must have
• Frontpage, Contact Page, Blog Page, about page and FAQ and Terms Page
• This will be on a wordpress site
Nice to have
• would like to have more of a female slant and feel. photos of workouts

```html
<!DOCTYPE html>
<html lang="en">
<head>
<meta charset="utf-8">
<title>harbor Kettrix</title>
<link href="https://fonts.googleapis.com/css2?family=Roboto:wght@300;400;500;700&display=swap" rel="stylesheet">
<style>
:root{
  --green:#9dc01e;
  --green-dark:#86a616;
  --ink:#2a2a2a;
  --dark:#232323;
  --dark-2:#313131;
  --text:#555;
  --muted:#888;
  --line:#e2e2e2;
  --cream:#f6f8ee;
  --white:#fff;
}
*{box-sizing:border-box;margin:0;padding:0}
html,body{width:1200px;height:3279px;overflow:hidden}
body{position:relative;font-family:'Roboto',Arial,sans-serif;color:var(--text);background:var(--white);font-size:12px;line-height:1.5}
.abs{position:absolute}
.hl{color:var(--green)}
.photo{position:absolute}
.btn{position:absolute;background:var(--green);color:#fff;font-weight:500;display:flex;align-items:center;justify-content:center}
.ico{display:inline-block;vertical-align:middle}

/* top bar & hero */
.hero{position:absolute;left:0;top:0;width:1200px;height:570px;background:linear-gradient(90deg,#1d1d1d 0%,#2c2c2c 45%,#4a4744 70%,#2a2a2a 100%)}
.hero .photo{left:560px;top:0;width:640px;height:570px;background:radial-gradient(ellipse at 45% 45%,#8a7a6a 0%,#4d4540 40%,#262626 80%)}
.topbar{position:absolute;left:81px;top:8px;width:1038px;height:22px;color:#eee;font-size:12px;display:flex;align-items:center;gap:26px}
.topbar .social{margin-left:auto;display:flex;gap:6px}
.dot{width:22px;height:22px;border-radius:50%;border:2px solid var(--green);display:inline-block}
.nav{position:absolute;left:81px;top:39px;width:1038px;height:81px;background:#fff;display:flex;align-items:center;padding:0 20px}
.brand{display:flex;align-items:center;gap:10px;font-size:20px;font-weight:500;color:var(--green)}
.brand .mark{width:28px;height:28px;background:var(--ink);border-radius:50%}
.menu{margin-left:auto;display:flex;gap:0;list-style:none;font-size:14px;color:#444}
.menu li{width:98px;text-align:center;line-height:81px}
.menu li.active{color:var(--green);border-top:3px solid var(--green);line-height:75px}
.slide-arrow{position:absolute;top:270px;width:22px;height:50px;background:rgba(255,255,255,.15);color:#ccc;font-size:16px;display:flex;align-items:center;justify-content:center}
.quote{position:absolute;left:81px;top:246px;color:#fff;font-size:33px;font-weight:700;line-height:1.42}
.hero .btn{left:81px;top:374px;width:227px;height:41px;font-size:19px}

/* intro panels */
.panel{position:absolute;top:500px;height:200px;padding:18px 20px}
.welcome{left:81px;width:343px;background:var(--green);color:#fff}
.welcome h3{font-size:18px;font-weight:400;margin-bottom:14px}
.welcome p{font-size:11px;line-height:1.7;color:#f1f6df}
.news{left:428px;width:342px;background:#ececec}
.news h3{font-size:18px;font-weight:400;color:#333;margin-bottom:14px}
.news .chev{position:absolute;right:20px;top:18px;color:#999;font-size:16px}
.news-item{display:flex;gap:10px;border-bottom:1px solid #d8d8d8;padding:8px 0;font-size:12px;color:#444}
.news-item .thumb{width:62px;height:44px;background:linear-gradient(135deg,#777,#333)}
.news-item small{display:block;font-size:10px;color:#888}
.corner{position:absolute;right:0;bottom:0;width:0;height:0;border-left:24px solid transparent;border-bottom:24px solid #fff}
.news .corner{border-bottom-color:var(--green)}
.newsletter{left:774px;width:345px;background:#1f1f1f;color:#fff;overflow:hidden}
.newsletter .photo{left:160px;top:0;width:185px;height:200px;background:linear-gradient(90deg,#1f1f1f,#5a5048 60%,#3a3330)}
.newsletter h3{position:relative;font-size:18px;font-weight:400;margin-bottom:10px}
.newsletter p{position:relative;font-size:11px;color:#ccc;margin-bottom:8px}
.field{display:block;width:165px;height:26px;border:1px solid #555;font-size:10px;color:#ccc;padding:5px 8px;margin-bottom:8px;position:relative;background:rgba(0,0,0,.3)}
.newsletter .btn{position:relative;width:165px;height:26px;font-size:11px}

/* guide cards */
.guides{position:absolute;left:0;top:739px;width:1200px;height:424px;background:var(--cream)}
.guide{position:absolute;top:48px;width:328px;height:328px;background:#fff;border:1px solid var(--line)}
.guide .photo{left:0;top:0;width:326px;height:197px}
.guide h4{position:absolute;left:13px;top:208px;color:var(--green);font-size:17px;font-weight:400}
.guide p{position:absolute;left:13px;top:238px;right:13px;font-size:11.5px;line-height:1.6;color:#666}

/* articles */
.articles{position:absolute;left:0;top:1163px;width:1200px;height:568px;background:linear-gradient(100deg,#262626,#3b3832 60%,#262626)}
.sec-title{position:absolute;font-size:25px;font-weight:400;color:#fff}
.article{position:absolute;left:81px;width:686px;height:192px}
.article .photo{left:0;top:0;width:304px;height:192px;background:linear-gradient(135deg,#555,#1e1e1e)}
.article .body{position:absolute;left:304px;top:0;width:382px;height:192px;background:#fff;padding:18px 18px}
.meta{font-size:10.5px;color:var(--green);font-style:italic;margin-bottom:12px}
.meta span{color:#999;margin:0 6px}
.body h5,.workout h5{font-size:12px;font-weight:500;color:#222;margin-bottom:6px;text-transform:uppercase}
.body p,.workout p{font-size:11px;line-height:1.65;color:#555}
.body p b,.workout p b{color:var(--green);font-weight:400}
.workout{position:absolute;left:791px;top:92px;width:328px;height:406px;background:#fff}
.workout .photo{left:0;top:0;width:328px;height:192px;background:linear-gradient(135deg,#7a7068,#2e2a28)}
.workout .txt{position:absolute;left:16px;top:210px;right:16px}
.workout .date{font-size:11px;color:var(--green);font-style:italic;margin-bottom:14px}

/* videos & team */
.media{position:absolute;left:0;top:1731px;width:1200px;height:459px;background:#fff}
.media .sec-title{color:#333}
.arrows{position:absolute;color:#aaa;font-size:16px;letter-spacing:6px}
.video{position:absolute;top:101px;width:328px}
.video .photo{position:relative;width:328px;height:186px;background:linear-gradient(135deg,#e7e2dc,#8b8580)}
.video .play{position:absolute;left:144px;top:72px;width:40px;height:36px;background:rgba(0,0,0,.6);border-radius:4px}
.video .play:after{content:"";position:absolute;left:15px;top:10px;border-left:13px solid #fff;border-top:8px solid transparent;border-bottom:8px solid transparent}
.controls{width:328px;height:37px;background:linear-gradient(#444,#1b1b1b);display:flex;align-items:center;padding:0 12px;gap:10px}
.controls .bar{flex:1;height:5px;background:#666;position:relative}
.controls .bar i{position:absolute;left:0;top:0;width:45%;height:5px;background:var(--green)}
.tri{width:0;height:0;border-left:9px solid #eee;border-top:6px solid transparent;border-bottom:6px solid transparent}
.video h6{margin-top:18px;font-size:13px;font-weight:500;color:#222}
.video p{margin-top:6px;font-size:11.5px;color:#666;line-height:1.6}
.team{position:absolute;left:791px;top:101px;width:328px}
.team .photo{position:relative;width:328px;height:197px;background:linear-gradient(135deg,#d9d6d0,#6b6762)}
.team .info{background:var(--green);color:#fff;padding:12px 14px;height:88px}
.team .info h6{font-size:14px;font-weight:500}
.team .info p{font-size:10.5px;color:#eef5d6;line-height:1.5}
.team .links{height:26px;background:#fff;border:1px solid var(--green);display:flex;justify-content:center}
.team .links i{width:36px;border-right:1px solid var(--green);display:flex;align-items:center;justify-content:center}
.team .links i:last-child{border-right:0}
.team .links i:after{content:"";width:10px;height:10px;border-radius:50%;background:var(--green)}

/* call to action */
.cta{position:absolute;left:0;top:2190px;width:1200px;height:243px;background:linear-gradient(90deg,#1e1e1e,#363636 50%,#1e1e1e)}
.cta p{position:absolute;left:150px;right:150px;top:56px;text-align:center;color:#fff;font-size:20px;line-height:1.55;font-weight:300}
.cta .btn{left:485px;top:147px;width:230px;height:39px;font-size:19px}

/* shop */
.shop h2{position:absolute;left:0;width:1200px;top:2464px;text-align:center;font-size:26px;font-weight:400;color:#333}
.product{position:absolute;top:2531px;width:234px;height:337px}
.product .photo{left:0;top:0;width:234px;height:289px;background:radial-gradient(ellipse at 50% 50%,#cfcfcf,#999)}
.product .tag{position:absolute;left:0;bottom:0;width:234px;height:48px;background:#3a3a3a;color:#fff;display:flex;align-items:center;justify-content:space-between;padding:0 18px;font-size:13.5px}
.product .tag b{font-size:16px;font-weight:500}

/* footer */
.footer{position:absolute;left:0;top:2918px;width:1200px;height:322px;background:linear-gradient(90deg,#262626,#383838 55%,#2a2a2a);color:#ddd}
.footer h4{position:absolute;font-size:19px;font-weight:500;color:#fff;display:flex;align-items:center;gap:10px}
.footer h4:after{content:"";position:absolute;left:0;top:34px;width:100%;height:1px;background:#666}
.ffield{position:absolute;border:1px solid #555;font-size:11px;color:#ccc;padding:10px 12px;background:rgba(0,0,0,.15)}
.footer .btn{font-size:14px}
.qlinks{position:absolute;left:627px;top:106px;list-style:none;font-size:12.5px;line-height:22.5px;color:#eee}
.qlinks li:before{content:"›";color:#bbb;margin-right:10px}
.qlinks li:first-child{color:#fff;font-weight:500}
.contact{position:absolute;left:868px;top:108px;width:250px;font-size:12px;color:#ddd}
.contact .row{display:flex;gap:10px;margin-bottom:18px;line-height:1.5}
.copy{position:absolute;left:0;top:3240px;width:1200px;height:39px;background:var(--green);color:#fff;font-size:11.5px;display:flex;align-items:center;padding:0 81px}
.copy .social{margin-left:auto;display:flex;gap:6px}
.copy .dot{border-color:#fff}
</style>
</head>
<body>

<section class="hero">
  <div class="photo" role="img" aria-label="Woman lifting dumbbells overhead in a dark gym"></div>
  <div class="topbar">
    <span><svg class="ico" width="14" height="10" viewBox="0 0 14 10"><rect x=".5" y=".5" width="13" height="9" fill="none" stroke="#9dc01e"/><path d="M.5 .5 7 6 13.5 .5" fill="none" stroke="#9dc01e"/></svg> info@harborKettrix.com</span>
    <span><svg class="ico" width="12" height="12" viewBox="0 0 12 12"><path d="M2 1h3l1 3-2 1a7 7 0 0 0 3 3l1-2 3 1v3c-6 1-10-4-9-9z" fill="#9dc01e"/></svg> 555-014-2290</span>
    <span class="social"><i class="dot"></i><i class="dot"></i><i class="dot"></i><i class="dot"></i></span>
  </div>
  <header class="nav">
    <div class="brand"><span class="mark"></span>harbor Kettrix</div>
    <ul class="menu">
      <li class="active">Home</li><li>About</li><li>Recipe</li><li>Exercise</li><li>FAQ's</li><li>Blog</li><li>Contact</li>
    </ul>
  </header>
  <div class="slide-arrow" style="left:0">‹</div>
  <div class="slide-arrow" style="right:0">›</div>
  <h1 class="quote">"if It Doesn't <span class="hl">Challenge</span> You<br>It Doesn's <span class="hl">Change</span> You"</h1>
  <div class="btn">Get Started</div>
</section>

<div class="panel welcome">
  <h3>Welcome to <b style="font-weight:500">harbor Kettrix</b></h3>
  <p>Lorem ipsum dolor sit amet, consectetuer adipiscing elit, sed diam nonummy nibh euismod tincidunt ut in laoreet dolore magna aliquam erat volutpat. Ut wisi enim ad minim venia m, quis nostrud exerci tationperq ullamcorper suscipit lobortis nisl ut.</p>
  <span class="corner"></span>
</div>
<div class="panel news">
  <h3>Latest <span class="hl">News</span></h3>
  <span class="chev">‹ ›</span>
  <div class="news-item"><span class="thumb" role="img" aria-label="Gym equipment"></span><div>Lorem ipsum dolor sit amet<small>23Mar2016</small></div></div>
  <div class="news-item"><span class="thumb" role="img" aria-label="Athlete training"></span><div>Lorem ipsum dolor sit amet<small>23Mar2016</small></div></div>
  <span class="corner"></span>
</div>
<div class="panel newsletter">
  <div class="photo" role="img" aria-label="Athlete training with a weight"></div>
  <h3>Newsletter <span class="hl">Signup</span></h3>
  <p>Lorem ipsum dolor sit amet</p>
  <span class="field">Name</span>
  <span class="field">Email</span>
  <span class="btn">Submit</span>
</div>

<section class="guides">
  <article class="guide" style="left:81px">
    <div class="photo" role="img" aria-label="Man doing dumbbell curls on a bench" style="background:linear-gradient(135deg,#3d6fa8,#1d2a3a)"></div>
    <h4>What to Expect</h4>
    <p>Lorem ipsum dolor sit amet, consectetuer adipiscing elit, sed diam nonummy nibh euismod tincidunt ut in laoreet dolore magna aliquam erat volutpat.</p>
  </article>
  <article class="guide" style="left:435px">
    <div class="photo" role="img" aria-label="Woman flipping a large tyre outdoors" style="background:linear-gradient(180deg,#a7bfd6,#6f8aa3 60%,#4e5a60)"></div>
    <h4>What to Wear</h4>
    <p>Lorem ipsum dolor sit amet, consectetuer adipiscing elit, sed diam nonummy nibh euismod tincidunt ut in laoreet dolore magna aliquam erat volutpat.</p>
  </article>
  <article class="guide" style="left:791px">
    <div class="photo" role="img" aria-label="Group of women lifting barbells in a gym" style="background:linear-gradient(135deg,#8a8580,#2b2826)"></div>
    <h4>How to Pick out a Kettrix Gym</h4>
    <p>Lorem ipsum dolor sit amet, consectetuer adipiscing elit, sed diam nonummy nibh euismod tincidunt ut in laoreet dolore magna aliquam erat volutpat.</p>
  </article>
</section>

<section class="articles">
  <h2 class="sec-title" style="left:81px;top:36px">Latest <span class="hl">Articles</span></h2>
  <h2 class="sec-title" style="left:791px;top:36px">Today's <span class="hl">Workout</span></h2>
  <article class="article" style="top:92px">
    <div class="photo" role="img" aria-label="Boxer kicking a heavy bag"></div>
    <div class="body">
      <div class="meta">23 Mar 2016<span>/</span>0 Comments</div>
      <h5>Lorem ipsum dolor consecte</h5>
      <p>Duis autem vel eum iriure dolor in hendreri inmo vulputate velit esse molestie consequatn vel illum dolore eu feugiat nulla facilisis Lorem ipsum dolor sit amet, consectetuer adipiscing elit, sed diam nonummy nibh euismod tincidunt ut in laoreet dolore magna aliquam erat volutpat... <b>[+]</b></p>
    </div>
  </article>
  <article class="article" style="top:308px">
    <div class="photo" role="img" aria-label="Man lifting dumbbells against a dark background" style="background:linear-gradient(135deg,#3a5570,#141c24)"></div>
    <div class="body">
      <div class="meta">23 Mar 2016<span>/</span>0 Comments</div>
      <h5>Lorem ipsum dolor consecte</h5>
      <p>Duis autem vel eum iriure dolor in hendreri inmo vulputate velit esse molestie consequatn vel illum dolore eu feugiat nulla facilisis Lorem ipsum dolor sit amet, consectetuer adipiscing elit, sed diam nonummy nibh euismod tincidunt ut in laoreet dolore magna aliquam erat volutpat... <b>[+]</b></p>
    </div>
  </article>
  <article class="workout">
    <div class="photo" role="img" aria-label="Group doing push-ups in a class"></div>
    <div class="txt">
      <h5>Lorem ipsum dolor consecte</h5>
      <div class="date">23 Mar 2016</div>
      <p>Duis autem vel eum iriure dolor in hendreri inmo vulputate velit esse molestie consequatn vel illum dolore eu feugiat nulla facilisis Lorem ipsum dolor sit amet, consectetuer adipiscing elit, sed diam nonummy nibh euismod tincidunt ut in laoreet dolore magna aliquam erat volutpat... <b>[+]</b></p>
    </div>
  </article>
</section>

<section class="media">
  <h2 class="sec-title" style="left:81px;top:40px">Latest <span class="hl">Videos</span></h2>
  <span class="arrows" style="left:738px;top:44px">‹ ›</span>
  <h2 class="sec-title" style="left:791px;top:40px">Our <span class="hl">Team</span></h2>
  <span class="arrows" style="left:1090px;top:44px">‹ ›</span>
  <div class="video" style="left:81px">
    <div class="photo" role="img" aria-label="Couple training with dumbbells"><span class="play"></span></div>
    <div class="controls"><span class="tri"></span><span class="bar"><i></i></span></div>
    <h6>Lorem ipsum dolor sit amet</h6>
    <p>Lorem ipsum dolor sit amet, consectetuer adipiscing elit. Aenean et dignissim sem, interdum risus.</p>
  </div>
  <div class="video" style="left:435px">
    <div class="photo" role="img" aria-label="Close-up of a dumbbell lift" style="background:linear-gradient(135deg,#b65a4a,#2a1a18)"><span class="play"></span></div>
    <div class="controls"><span class="tri"></span><span class="bar"><i></i></span></div>
    <h6>Lorem ipsum dolor sit amet</h6>
    <p>Lorem ipsum dolor sit amet, consectetuer adipiscing elit. Aenean et dignissim sem, interdum risus.</p>
  </div>
  <div class="team">
    <div class="photo" role="img" aria-label="Team member in boxing training"></div>
    <div class="info">
      <h6>Rena Calloway</h6>
      <p>Duis autem vel eum iriure dolor in hendrerit inmiputate velit esse molestie consequat vel</p>
    </div>
    <div class="links"><i></i><i></i><i></i></div>
  </div>
</section>

<section class="cta">
  <p>Lorem ipsum dolor sit amet, consectetuer adipiscing elit, sed diam nonummy nibheuism od tincidunt ut in laoreet dolore magna</p>
  <div class="btn">Get Started</div>
</section>

<section class="shop">
  <h2>Shop <span class="hl">harbor Kettrix</span></h2>
  <div class="product" style="left:81px"><div class="photo" role="img" aria-label="Protein supplement tub"></div><div class="tag">Lorem ipsum dolor<b>$65</b></div></div>
  <div class="product" style="left:348px"><div class="photo" role="img" aria-label="Treadmill"></div><div class="tag">Lorem ipsum dolor<b>$65</b></div></div>
  <div class="product" style="left:614px"><div class="photo" role="img" aria-label="Pre-workout supplement tub"></div><div class="tag">Lorem ipsum dolor<b>$65</b></div></div>
  <div class="product" style="left:881px"><div class="photo" role="img" aria-label="Weight plate rack"></div><div class="tag">Lorem ipsum dolor<b>$65</b></div></div>
</section>

<footer class="footer">
  <h4 style="left:81px;top:56px;width:222px"><svg width="20" height="20" viewBox="0 0 20 20"><circle cx="10" cy="10" r="8.5" fill="none" stroke="#fff" stroke-width="2"/><text x="10" y="14.5" font-size="12" text-anchor="middle" fill="#fff" font-family="Roboto,sans-serif" font-weight="700">?</text></svg>Quick Inquiry</h4>
  <span class="ffield" style="left:81px;top:114px;width:225px;height:37px">Name</span>
  <span class="ffield" style="left:81px;top:173px;width:225px;height:37px">Email Address</span>
  <span class="ffield" style="left:81px;top:230px;width:225px;height:37px">Phone Number</span>
  <span class="ffield" style="left:324px;top:114px;width:286px;height:96px">Message</span>
  <span class="btn" style="left:324px;top:230px;width:286px;height:37px">Submit</span>

  <h4 style="left:627px;top:56px;width:180px"><svg width="16" height="18" viewBox="0 0 16 18"><rect x="1" y="2" width="14" height="15" fill="none" stroke="#fff" stroke-width="2"/><path d="M4 7h8M4 10h8M4 13h6" stroke="#fff" stroke-width="1.5"/></svg>Quick Links</h4>
  <ul class="qlinks"><li>Home</li><li>About</li><li>Recipe</li><li>Exercise</li><li>FAQ's</li><li>Blog</li><li>Contact</li></ul>

  <h4 style="left:868px;top:56px;width:250px"><svg width="18" height="18" viewBox="0 0 18 18"><circle cx="9" cy="9" r="8" fill="none" stroke="#fff" stroke-width="2"/><path d="M1 9h16M9 1c-4 4-4 12 0 16M9 1c4 4 4 12 0 16" fill="none" stroke="#fff" stroke-width="1.3"/></svg>Contact Information</h4>
  <div class="contact">
    <div class="row"><svg width="12" height="16" viewBox="0 0 12 16"><path d="M6 0a6 6 0 0 0-6 6c0 4 6 10 6 10s6-6 6-10a6 6 0 0 0-6-6z" fill="#9dc01e"/><circle cx="6" cy="6" r="2.2" fill="#2c2c2c"/></svg><div><b style="font-weight:500;color:#fff">harbor Kettrix,</b><br>Lorem ipsum dolor sit amet, consec tetuer adipiscing elit, sed</div></div>
    <div class="row"><svg width="13" height="13" viewBox="0 0 12 12"><path d="M2 1h3l1 3-2 1a7 7 0 0 0 3 3l1-2 3 1v3c-6 1-10-4-9-9z" fill="#9dc01e"/></svg><span>555-014-2290</span></div>
    <div class="row"><svg width="14" height="10" viewBox="0 0 14 10"><rect width="14" height="10" fill="#9dc01e"/><path d="M0 0 7 6 14 0" fill="none" stroke="#2c2c2c"/></svg><span style="font-size:11px">info@harborKettrix.com</span></div>
  </div>
</footer>

<div class="copy">Copyright © 2016 harbor Kettrix. All Rights Reserved.
  <span class="social"><i class="dot"></i><i class="dot"></i><i class="dot"></i><i class="dot"></i></span>
</div>

</body>
</html>
```